Design a Unique and Eye-Catching Necklace Card for Wendaray's New Brightwell Line

Attention all creative minds from around the world! Wendaray, a company known for its free-spirited and bohemian chic vibe, is proud to announce a new design contest. We are inviting you to create a dynamic and unique necklace card for our upcoming Brightwell line.

Our new Brightwell line comprises 12-20 unique necklace combinations. Each necklace features different stones, each with its own healing properties and associated zodiac sign. We are looking for a template that can be easily modified to change the names of the stones, zodiac sign, and the colors to match the specific stones on each necklace.

The card should be 3 x 4,
It should include the names of the stones, the associated zodiac sign (if applicable), a few words about the healing properties of the stones, and a captivating graphic that represents the colors of the stones.

Our goal is to delight our customers with packaging as unique as the necklaces themselves. The necklace should be the focal point, but the text and graphic on the card should also draw the eye.

Please note that our target audience includes mid-priced boutiques across the country and festival-goers in Colorado. Your design should reflect the unique taste and free spirit of our clientele.

We are excited to see your creativity shine in this project. If there are any points that need clarification, please do not hesitate to ask. We look forward to your participation in bringing the Brightwell line to life!
https://www.draftnook.example/board/KQ7mPzR2tLw/edit

https://www.draftnook.example/board/VJ3nHsX8qYb/edit
I want to use the flowing watercolor and have it change with each necklace color.
Use the necklaces below. Incorporate the zodiac symbol as is shown below.

Examples of other cards in our collection

The Little Pebble Pendant: https://www.draftnook.example/board/TB5wGdM4cRu/edit

Other examples of necklace cards I like:

https://www.craftbazaro.example/item/731905284/green-stone-pendant

https://www.craftbazaro.example/item/462918037/birthstone-pendant-green

https://www.craftbazaro.example/item/2907315628/crystal-bead-bracelets

https://www.craftbazaro.example/item/3816402795/dark-stone-guard-pendant

Target Market(s)

Women aged 25-50 with a spiritual, hippy, bohemain, yoga vibe.

Industry/Entity Type

Handmade Jewelry | Wholesale jewelry | Retail Jewelry sales at Festivals

Font styles to use
Script

Colors

Designer to choose colors to be used in the design.

Requirements
Must have
• A template that can be interchangable with the stone colors, names and healing properties.
Nice to have
• Some different ideas about the graphic color patterns on the card.
Should not have
• Any graphic that would cover the middle of the necklace card and keep people from seeing the neckalce

```html
<!DOCTYPE html>
<html lang="en">
<head>
<meta charset="utf-8">
<title>Ocean Jasper Necklace Card</title>
<link href="https://fonts.googleapis.com/css2?family=Cinzel:wght@700&family=Cormorant+Garamond:wght@600&display=swap" rel="stylesheet">
<style>
  :root {
    --backdrop: #ece8e1;
    --card: #f7f8f7;
    --teal: #1e9fb3;
    --orange: #e4621f;
    --green: #2f8a3f;
    --red: #cc2027;
    --title: #2f7f86;
    --ink: #3a3a3c;
  }
  * { box-sizing: border-box; margin: 0; padding: 0; }
  html, body { width: 1200px; height: 1142px; overflow: hidden; }
  body { background: var(--backdrop); position: relative; }

  .necklace-card {
    position: absolute; left: 120px; top: 126px;
    width: 960px; height: 890px;
    background: var(--card);
    box-shadow: 0 6px 18px rgba(0,0,0,0.12);
    overflow: hidden;
  }
  .frame { position: absolute; left: 48px; top: 42px; width: 864px; height: 600px; }
  .frame-top {
    position: absolute; left: 0; top: 0; width: 100%; height: 4px;
    background: linear-gradient(90deg, var(--red), var(--green) 35%, var(--teal) 60%, var(--orange));
  }
  .frame-left { position: absolute; left: 0; top: 0; width: 4px; height: 100%; background: var(--red); }
  .frame-right { position: absolute; right: 0; top: 0; width: 4px; height: 100%; background: var(--orange); }

  .stone-name {
    position: absolute; left: 0; right: 0; top: 92px;
    text-align: center;
    font-family: 'Cinzel', serif; font-weight: 700;
    font-size: 72px; letter-spacing: 2px; line-height: 1;
    color: var(--title);
  }

  .necklace-photo {
    position: absolute; left: 170px; top: 210px; width: 620px; height: 320px;
    background: radial-gradient(ellipse at 50% 85%, rgba(196,92,54,0.35), rgba(47,120,112,0.22) 55%, rgba(247,248,247,0) 75%);
    border-radius: 8px;
  }

  .healing-note {
    position: absolute; left: 0; right: 0; top: 556px;
    text-align: center;
    font-family: 'Cormorant Garamond', serif; font-weight: 600;
    font-size: 38px; line-height: 1.1; letter-spacing: 0.5px;
    color: var(--ink); text-transform: uppercase;
  }

  .watercolor-band { position: absolute; left: 0; bottom: 0; width: 960px; height: 236px; }
</style>
</head>
<body>
  <div class="necklace-card">
    <div class="frame">
      <div class="frame-top"></div>
      <div class="frame-left"></div>
      <div class="frame-right"></div>
    </div>

    <h1 class="stone-name">Ocean Jasper</h1>

    <div class="necklace-photo" role="img" aria-label="Photo of the ocean jasper bead necklace, teal and green beads fading to amber and red at the centre"></div>

    <p class="healing-note">Anti inflammatory &amp; reduces<br>pain from arthritis</p>

    <svg class="watercolor-band" viewBox="0 0 960 236" role="img" aria-label="Flowing watercolour band in green, yellow, orange and red matching the stone colours">
      <defs>
        <linearGradient id="bandTone" x1="0" y1="0" x2="1" y2="0.3">
          <stop offset="0" stop-color="#b7c23a"/>
          <stop offset="0.3" stop-color="#e6a22a"/>
          <stop offset="0.55" stop-color="#e24a22"/>
          <stop offset="0.8" stop-color="#f0a530"/>
          <stop offset="1" stop-color="#8fb04a"/>
        </linearGradient>
      </defs>
      <path d="M0 12 C180 0 330 30 470 70 C620 100 800 50 960 6 L960 236 L0 236 Z" fill="url(#bandTone)"/>
    </svg>
  </div>
</body>
</html>
```